Wordpress website update with basic ecomm features

We need an update to our existing website
www.quillharbour.com.au that can be easily updated, enhances our logo and can take payments online and a basic text logo suite for 3 products. Website would reflect confidence and give clients confidence in the outcomes we will provide for them. must be easy to use, crisp, fresh, clean and dynamic.

Target Market(s)

entrepreneurs, professionals, small business owners, corporate organisations, universities

Industry/Entity Type

Online

Coding

Coded - Design and coding required

Number of Pages Required

5+ page

Font styles to use
Sans Serif

Requirements
Must have
• be easy to navigate, look professional, please see brief doc
Nice to have
• please see briefing doc
Should not have
• please see briefing doc

```html
<!DOCTYPE html>
<html lang="en">
<head>
<meta charset="utf-8">
<title>Quill Harbour</title>
<link href="https://fonts.googleapis.com/css2?family=Lato:wght@400;700;900&family=Oswald:wght@400;500&display=swap" rel="stylesheet">
<style>
:root{
  --blue:#27b6ec;
  --ink:#2f2f2f;
  --text:#555;
  --muted:#888;
  --grey:#ececec;
  --dark:#262626;
  --white:#fff;
  --shirt:#9ccbe8;
  --suit:#3a3f48;
  --wall:#eef1f3;
}
*{box-sizing:border-box;margin:0;padding:0}
html,body{width:1200px;height:2564px;overflow:hidden}
body{position:relative;background:var(--white);font-family:'Lato',sans-serif;color:var(--text)}
.photo{position:absolute}

/* top bar */
.topbar{position:absolute;left:0;top:0;width:1200px;height:30px}
.topbar .contact{position:absolute;top:9px;font-size:11px;color:var(--ink);display:flex;align-items:center;gap:8px}
.topbar .contact svg{width:14px;height:12px}
.social-strip{position:absolute;left:830px;top:0;width:197px;height:30px;background:var(--blue);display:flex;justify-content:space-around;align-items:center;padding:0 10px}
.social-strip span{width:11px;height:11px;border-radius:50%;background:var(--white)}

/* header */
.header{position:absolute;left:0;top:30px;width:1200px;height:87px;border-bottom:1px solid #ddd}
.brand{position:absolute;left:172px;top:19px;display:flex;align-items:center;gap:10px}
.brand-mark{width:44px;height:44px;background:var(--blue);border-radius:3px}
.brand-name{font-weight:900;font-size:17px;letter-spacing:3px;color:var(--blue);line-height:18px}
.nav-item{position:absolute;top:16px;transform:translateX(-50%);text-align:center;font-size:12px;color:var(--ink);white-space:nowrap}
.nav-item svg{display:block;margin:0 auto 9px;width:26px;height:26px}
.nav-item.active{color:var(--blue)}

/* hero */
.hero{position:absolute;left:0;top:117px;width:1200px;height:381px;background:#f3f3f3;overflow:hidden}
.hero-photo{left:640px;top:0;width:560px;height:381px;
  background:
    radial-gradient(ellipse 150px 130px at 330px 280px,var(--shirt) 0%,rgba(156,203,232,.7) 50%,rgba(156,203,232,0) 100%),
    radial-gradient(ellipse 110px 190px at 500px 210px,#c9d0d6 0%,rgba(201,208,214,0) 100%),
    radial-gradient(ellipse 180px 60px at 250px 360px,#e6e9eb 0%,rgba(230,233,235,0) 100%),
    linear-gradient(90deg,#f3f3f3 0%,#eef1f2 30%,#f4f6f7 60%,#dfe4e7 100%);}
.hero-title{position:absolute;left:172px;top:108px;font-family:'Oswald',sans-serif;font-weight:500;font-size:40px;color:var(--blue);line-height:1}
.hero-text{position:absolute;left:172px;top:153px;width:408px;font-size:16px;line-height:19.5px;color:var(--text)}
.btn{position:absolute;display:flex;align-items:center;justify-content:center;background:var(--blue);color:var(--white);font-size:11px;text-transform:uppercase}
.hero .btn{top:228px;width:124px;height:35px}

/* about */
.section-title{font-weight:900;font-size:18px;color:var(--blue)}
.about-title{position:absolute;left:172px;top:546px}
.about-copy{position:absolute;left:172px;top:575px;width:485px;font-size:11px;line-height:13.8px;color:var(--text)}
.about-copy p+p{margin-top:10px}
.about-gallery{position:absolute;left:172px;top:713px;width:489px;height:109px;background:var(--grey);display:flex;gap:14px;padding:8px 10px}
.about-gallery div{flex:1;border:2px solid var(--white)}
.tabs{position:absolute;left:684px;top:549px;width:343px;height:36px;display:flex;gap:3px}
.tab{flex:1;background:var(--dark);color:var(--white);font-size:10px;text-align:center;display:flex;align-items:center;justify-content:center;line-height:11px;text-transform:uppercase}
.tab.active{background:var(--blue);position:relative}
.tab.active::after{content:"";position:absolute;bottom:-7px;left:50%;margin-left:-7px;border:7px solid transparent;border-bottom:0;border-top-color:var(--blue)}
.program-list{position:absolute;left:684px;top:598px;width:343px;list-style:none;font-size:11px;line-height:14.8px;color:var(--text)}
.program-list li{padding-left:18px;position:relative}
.program-list li::before{content:"";position:absolute;left:1px;top:4px;width:6px;height:6px;background:var(--blue);transform:rotate(45deg)}
.pillars{position:absolute;left:684px;top:783px;width:343px;display:grid;grid-template-columns:168px 1fr;font-size:10px;line-height:13px;color:var(--muted);text-transform:uppercase}

/* services */
.services{position:absolute;left:0;top:887px;width:1200px;height:276px;background:var(--blue)}
.service-card{position:absolute;top:39px;width:197px;height:197px;background:var(--white);text-align:center;padding-top:16px}
.service-card svg{width:38px;height:38px;display:block;margin:0 auto}
.service-card h3{font-size:12px;font-weight:900;color:var(--ink);margin-top:12px}
.service-card p{font-size:10.5px;line-height:13.5px;color:var(--text);margin:10px 12px 0}
.service-card .btn{position:static;margin:10px auto 0;width:94px;height:20px;text-transform:none;font-size:10px}

/* gallery */
.feature-tile{position:absolute;left:172px;top:1241px;width:197px;height:131px;background:linear-gradient(135deg,#5fc9ef,#3bb8e6 60%,#7fd0ec);text-align:center;color:var(--white);padding-top:18px}
.feature-tile h3{font-size:12px;font-weight:900}
.feature-tile p{font-size:10.5px;line-height:13px;font-weight:700;margin:3px 10px 0}
.feature-tile span{display:inline-block;margin-top:6px;background:var(--white);color:var(--blue);font-size:10px;width:94px;height:20px;line-height:20px}
.gallery-photo{border:1px solid #ddd}

/* testimonial */
.testimonial{position:absolute;left:0;top:1612px;width:1200px;height:401px;background:var(--grey);text-align:center}
.avatar{position:absolute;left:549px;top:63px;width:102px;height:102px;border-radius:50%;background:radial-gradient(circle at 50% 55%,#c79c88 0%,#8a5444 55%,#e9e4df 100%);border:3px solid #ddd}
.testimonial .name{position:absolute;left:0;width:1200px;top:184px;font-size:14px;font-weight:700;color:var(--blue)}
.testimonial .quote{position:absolute;left:255px;width:690px;top:205px;font-size:11.5px;line-height:15px;font-weight:700;color:#444}
.testimonial .role{position:absolute;left:0;width:1200px;top:271px;font-size:13px;font-style:italic;font-weight:700;color:var(--ink)}
.stars{position:absolute;left:560px;top:292px;width:80px;height:16px}
.dots{position:absolute;left:555px;top:332px;display:flex;gap:14px}
.dots span{width:22px;height:4px;border-radius:2px;background:var(--ink)}
.dots span.on{background:var(--blue)}

/* contact */
.contact-band{position:absolute;left:0;top:2013px;width:1200px;height:407px;background:var(--blue);color:var(--white);text-align:center}
.contact-band h2{position:absolute;left:0;width:1200px;top:36px;font-size:19px;font-weight:900}
.contact-band .rule{position:absolute;left:575px;top:69px;width:50px;height:3px;background:var(--white)}
.contact-band .intro{position:absolute;left:370px;width:460px;top:90px;font-size:10.5px;line-height:13px}
.contact-item{position:absolute;top:138px;transform:translateX(-50%);font-size:11px;font-weight:700;white-space:nowrap}
.contact-item svg{display:block;margin:0 auto 8px;width:18px;height:18px}
.field{position:absolute;background:var(--white);font-size:10px;color:#999;padding:6px 8px;text-align:left}
.form-btn{position:absolute;top:332px;height:28px;display:flex;align-items:center;justify-content:center;font-size:11px;font-weight:700;color:var(--white)}

/* footer */
.footer{position:absolute;left:0;top:2420px;width:1200px;height:113px;background:var(--dark);text-align:center;color:#ddd;font-size:9px}
.footer .links{position:absolute;left:0;width:1200px;line-height:12px}
.footer .icons{position:absolute;left:500px;top:64px;display:flex;gap:12px}
.footer .icons span{width:24px;height:24px;border-radius:3px}
.copyright{position:absolute;left:0;top:2533px;width:1200px;height:31px;background:var(--blue);color:var(--white);font-size:9px;text-align:center;line-height:31px}
</style>
</head>
<body>

<div class="topbar">
  <div class="contact" style="left:172px">
    <svg viewBox="0 0 14 12"><rect x="0.5" y="0.5" width="13" height="11" fill="#555"/><path d="M1 1l6 5 6-5" stroke="#fff" fill="none"/></svg>
    info@quillharbour.com.au
  </div>
  <div class="contact" style="left:325px">
    <svg viewBox="0 0 14 14"><path d="M3 1l3 3-2 2c1 2 2 3 4 4l2-2 3 3-2 2C6 13 1 8 1 3z" fill="#555"/></svg>
    000 111 222 333 444
  </div>
  <div class="social-strip"><span></span><span></span><span></span><span></span><span></span><span></span><span></span></div>
</div>

<header class="header">
  <div class="brand"><div class="brand-mark"></div><div class="brand-name">QUILL<br>HARBOUR</div></div>
  <nav>
    <div class="nav-item active" style="left:480px"><svg viewBox="0 0 26 26"><path d="M3 13L13 4l10 9" stroke="#27b6ec" stroke-width="2.5" fill="none"/><path d="M6 12v11h5v-6h4v6h5V12" fill="#27b6ec"/></svg>HOME</div>
    <div class="nav-item" style="left:550px"><svg viewBox="0 0 26 26"><circle cx="13" cy="13" r="11" stroke="#333" stroke-width="2" fill="none"/><circle cx="13" cy="10" r="3.5" fill="#333"/><path d="M7 19c1-4 11-4 12 0z" fill="#333"/></svg>ABOUT US</div>
    <div class="nav-item" style="left:624px"><svg viewBox="0 0 26 26"><circle cx="13" cy="13" r="11" fill="#333"/><path d="M8 13l4 4 6-8" stroke="#fff" stroke-width="2.5" fill="none"/></svg>WHY US</div>
    <div class="nav-item" style="left:689px"><svg viewBox="0 0 26 26"><path d="M2 14h6l4-3h7c2 0 2 3 0 3h-5" stroke="#333" stroke-width="2" fill="none"/><path d="M8 20h10l6-6" stroke="#333" stroke-width="2" fill="none"/><rect x="14" y="3" width="8" height="6" fill="#333"/></svg>OFFER</div>
    <div class="nav-item" style="left:745px"><svg viewBox="0 0 26 26"><circle cx="13" cy="13" r="11" stroke="#333" stroke-width="2" fill="none"/><path d="M9.5 10a3.5 3.5 0 1 1 5 3c-1.5 1-1.5 2-1.5 3" stroke="#333" stroke-width="2" fill="none"/><circle cx="13" cy="19.5" r="1.3" fill="#333"/></svg>FAQS</div>
    <div class="nav-item" style="left:824px"><svg viewBox="0 0 26 26"><path d="M13 3C6 3 2 7 2 12c0 3 2 5 4 6l-1 5 6-4h2c7 0 11-4 11-8S20 3 13 3z" fill="#333"/><circle cx="8" cy="12" r="1.5" fill="#fff"/><circle cx="13" cy="12" r="1.5" fill="#fff"/><circle cx="18" cy="12" r="1.5" fill="#fff"/></svg>TESTIMONIALS</div>
    <div class="nav-item" style="left:909px"><svg viewBox="0 0 26 26"><rect x="4" y="3" width="18" height="21" stroke="#333" stroke-width="2" fill="none"/><rect x="7" y="7" width="6" height="5" fill="#333"/><path d="M15 8h4M7 15h12M7 19h12" stroke="#333" stroke-width="2"/></svg>EVENTS</div>
    <div class="nav-item" style="left:991px"><svg viewBox="0 0 26 26"><rect x="2" y="6" width="22" height="15" fill="#333"/><path d="M3 7l10 8 10-8" stroke="#fff" stroke-width="1.5" fill="none"/></svg>CONTACT US</div>
  </nav>
</header>

<section class="hero">
  <div class="photo hero-photo" role="img" aria-label="Businessman in a light blue shirt on the phone at an office desk beside a computer monitor"></div>
  <h1 class="hero-title">GROW YOUR BUSINESS</h1>
  <p class="hero-text">Phasellus lorem enim, luctus ut velit eget, convallis egestas eros. Sed ornare ligula eget tortor tempor, quis porta tellus dictum. Phasellus lorem enim luctus ut velit eget.</p>
  <a class="btn" style="left:172px">Services</a>
  <a class="btn" style="left:318px">Read More</a>
</section>

<h2 class="section-title about-title">ABOUT US</h2>
<div class="about-copy">
  <p>The Quill Harbour builds and develops validation and innovation programs, communities and data to improve the overall success rate of entrepreneurial and early-stage ventures. Our aim is to build a flourishing innovation and collaboration eco-system that validates people, business &amp; society.</p>
  <p>The Quill Harbour takes the value created from the 4 early stage venture institutions (Incubators, Angel Investors, Accelerators, Hybrids – Northfield Business Review) and adds the power of the experience and shared economies to deliver personal and venture outcomes for all, not just a few – becoming a powerful Quill Harbour including:</p>
</div>
<div class="about-gallery">
  <div role="img" aria-label="Business team in a meeting" style="background:radial-gradient(ellipse 40px 45px at 60% 60%,#2e3440 0%,rgba(46,52,64,0) 100%),radial-gradient(ellipse 35px 40px at 25% 65%,#d9dde2 0%,rgba(217,221,226,0) 100%),linear-gradient(180deg,#eef3f7,#c9d6e0)"></div>
  <div role="img" aria-label="Hands holding a smartphone" style="background:radial-gradient(ellipse 30px 38px at 50% 45%,#c9d4dd 0%,rgba(201,212,221,0) 100%),radial-gradient(ellipse 50px 30px at 40% 80%,#b08f7e 0%,rgba(176,143,126,0) 100%),linear-gradient(135deg,#7f8b96,#2f3740)"></div>
  <div role="img" aria-label="Laptop and documents on a desk" style="background:radial-gradient(ellipse 45px 25px at 50% 70%,#ffffff 0%,rgba(255,255,255,0) 100%),radial-gradient(ellipse 40px 30px at 60% 35%,#3d4a57 0%,rgba(61,74,87,0) 100%),linear-gradient(135deg,#e7edf3,#a9bccb)"></div>
</div>

<div class="tabs">
  <div class="tab active">Outline of<br>Program</div>
  <div class="tab">What we<br>deliver</div>
  <div class="tab">Outcomes</div>
  <div class="tab">Agenda</div>
</div>
<ul class="program-list">
  <li>Best practice business education</li>
  <li>Expert facilitation that applies learning real-time to ventures and opportunities</li>
  <li>Real collaboration in an environment of trust, from day one</li>
  <li>Venture, personal &amp; social outcomes</li>
  <li>Shared resourcing</li>
  <li>Powerful networks</li>
  <li>Investment &amp; industry partnerships</li>
  <li>Informal and formal meet-ups</li>
  <li>Coaching to ensure focus and continued venture progress</li>
  <li>Community, not simply network, of like-minded individuals</li>
</ul>
<div class="pillars">
  <span>:: Strong Team</span><span>:: Real Opportunity</span>
  <span>:: Business Fundamentals</span><span>:: Innovation</span>
  <span>:: Acceleration &nbsp;Community</span><span></span>
</div>

<section class="services">
  <div class="service-card" style="left:172px">
    <svg viewBox="0 0 38 38"><circle cx="19" cy="19" r="16" stroke="#333" stroke-width="3" fill="none"/><path d="M26 12l-4 10-10 4 4-10z" fill="#333"/><circle cx="19" cy="19" r="2" fill="#fff"/></svg>
    <h3>BUSINESS PLAN</h3>
    <p>The Quill Harbour builds and develops validation and innovation programs, communities and data to improve the overall success rate .</p>
    <a class="btn">Read More</a>
  </div>
  <div class="service-card" style="left:391px">
    <svg viewBox="0 0 38 38"><rect x="4" y="8" width="24" height="26" stroke="#333" stroke-width="3" fill="none"/><path d="M14 24l2-6 14-14 4 4-14 14z" fill="#333"/></svg>
    <h3>BUSINESS PLAN</h3>
    <p>The Quill Harbour builds and develops validation and innovation programs, communities and data to improve the overall success rate .</p>
    <a class="btn">Read More</a>
  </div>
  <div class="service-card" style="left:610px">
    <svg viewBox="0 0 38 38"><path d="M19 3a11 11 0 0 0-6 20v5h12v-5a11 11 0 0 0-6-20z" stroke="#333" stroke-width="3" fill="none"/><path d="M14 32h10M16 36h6" stroke="#333" stroke-width="3"/></svg>
    <h3>BUSINESS PLAN</h3>
    <p>The Quill Harbour builds and develops validation and innovation programs, communities and data to improve the overall success rate .</p>
    <a class="btn">Read More</a>
  </div>
  <div class="service-card" style="left:830px">
    <svg viewBox="0 0 38 38"><rect x="6" y="3" width="26" height="32" stroke="#333" stroke-width="3" fill="none"/><rect x="10" y="7" width="18" height="7" fill="#333"/><g fill="#333"><rect x="10" y="17" width="4" height="4"/><rect x="17" y="17" width="4" height="4"/><rect x="24" y="17" width="4" height="4"/><rect x="10" y="24" width="4" height="4"/><rect x="17" y="24" width="4" height="4"/><rect x="24" y="24" width="4" height="7"/></g></svg>
    <h3>BUSINESS PLAN</h3>
    <p>The Quill Harbour builds and develops validation and innovation programs, communities and data to improve the overall success rate .</p>
    <a class="btn">Read More</a>
  </div>
</section>

<div class="feature-tile">
  <h3>BUSINESS PLAN</h3>
  <p>The Quill Harbour builds and develops validation and innovation programs, communities and data to improve the overall success rate.</p>
  <span>Read More</span>
</div>
<div class="photo gallery-photo" role="img" aria-label="Office interior with a person standing by tall windows" style="left:172px;top:1398px;width:197px;height:130px;background:radial-gradient(ellipse 40px 70px at 45% 55%,#2f2d2a 0%,rgba(47,45,42,0) 100%),radial-gradient(ellipse 60px 50px at 75% 30%,#e7e4dc 0%,rgba(231,228,220,0) 100%),linear-gradient(135deg,#6f6d68,#b9b6ae 55%,#3f3d39)"></div>
<div class="photo gallery-photo" role="img" aria-label="Smiling business team in suits gathered around a laptop on a white table" style="left:391px;top:1241px;width:417px;height:287px;background:radial-gradient(ellipse 150px 40px at 50% 92%,#f6f6f6 0%,rgba(246,246,246,0) 100%),radial-gradient(ellipse 230px 90px at 55% 68%,var(--suit) 0%,rgba(58,63,72,.6) 60%,rgba(58,63,72,0) 100%),radial-gradient(ellipse 80px 50px at 15% 60%,#e9ecef 0%,rgba(233,236,239,0) 100%),linear-gradient(180deg,#b8d6ea 0%,#9cbdd6 30%,#6f8599 55%,#545b66 80%,#e2e4e6 100%)"></div>
<div class="photo gallery-photo" role="img" aria-label="Business partners shaking hands across a meeting table" style="left:830px;top:1241px;width:197px;height:131px;background:radial-gradient(ellipse 70px 45px at 55% 60%,#343a42 0%,rgba(52,58,66,0) 100%),radial-gradient(ellipse 60px 20px at 50% 88%,#f0f2f4 0%,rgba(240,242,244,0) 100%),linear-gradient(135deg,#d6e1e9,#93a5b3 55%,#4a535c)"></div>
<div class="photo gallery-photo" role="img" aria-label="Colleagues shaking hands in a bright glass office" style="left:830px;top:1398px;width:197px;height:130px;background:radial-gradient(ellipse 75px 50px at 50% 62%,#333a44 0%,rgba(51,58,68,0) 100%),radial-gradient(ellipse 40px 40px at 85% 55%,#a85a4e 0%,rgba(168,90,78,0) 100%),linear-gradient(135deg,#e1edf4,#a6bccc 50%,#5b6772)"></div>

<section class="testimonial">
  <div class="avatar" role="img" aria-label="Portrait of the company CEO"></div>
  <div class="name">JOHN DOE</div>
  <p class="quote">Phasellus lorem enim, luctus ut velit eget, convallis egestas eros. Sed ornare ligula eget tortor tempor, quis porta tellus dictum. Phasellus lorem enim, luctus ut velit eget, convallis egestas eros. Sed ornare ligula eget tortor tempor, quis porta tellus dictum quis porta tellus dictum.</p>
  <div class="role">CEO OF QUILL HARBOUR</div>
  <svg class="stars" viewBox="0 0 80 16" aria-label="Five stars">
    <g fill="#27b6ec">
      <path id="st" d="M8 0l2.4 5 5.6.6-4.2 3.8 1.2 5.6L8 12.2 3 15l1.2-5.6L0 5.6 5.6 5z"/>
      <use href="#st" x="16"/><use href="#st" x="32"/><use href="#st" x="48"/><use href="#st" x="64"/>
    </g>
  </svg>
  <div class="dots"><span class="on"></span><span></span><span></span></div>
</section>

<section class="contact-band">
  <h2>GET IN TOUCH</h2>
  <div class="rule"></div>
  <p class="intro">Ut telloribus eget elenetum vel curleif end elit. Aean auctoetnlir pls. Nulla fn nec ero ante ipsummis fauulet utrice posere cubtsed leo pharetu nec augue.</p>
  <div class="contact-item" style="left:379px"><svg viewBox="0 0 18 18"><rect x="1" y="4" width="16" height="11" stroke="#fff" stroke-width="1.5" fill="none"/><path d="M1 4l8 6 8-6" stroke="#fff" stroke-width="1.5" fill="none"/></svg>hello@quillharbour.com.au</div>
  <div class="contact-item" style="left:600px"><svg viewBox="0 0 18 18"><path d="M9 1a6 6 0 0 0-6 6c0 4 6 10 6 10s6-6 6-10a6 6 0 0 0-6-6z" fill="#fff"/><circle cx="9" cy="7" r="2" fill="#27b6ec"/></svg>14 Wharf Lane, Harbourside NSW 2000 Australia</div>
  <div class="contact-item" style="left:814px"><svg viewBox="0 0 18 18"><path d="M4 1l4 4-2 2c1 2 3 4 5 5l2-2 4 4-2 3C8 17 1 10 1 4z" fill="#fff"/></svg>+61 2 5550 0142</div>
  <div class="field" style="left:306px;top:203px;width:289px;height:26px">Name</div>
  <div class="field" style="left:306px;top:245px;width:289px;height:26px">Email</div>
  <div class="field" style="left:306px;top:284px;width:289px;height:26px">Subject</div>
  <div class="field" style="left:610px;top:203px;width:289px;height:108px">Message</div>
  <div class="form-btn" style="left:492px;width:110px;background:#222">RESET</div>
  <div class="form-btn" style="left:619px;width:111px;border:1px solid #fff">SUBMIT</div>
</section>

<footer class="footer">
  <div class="links" style="top:22px">Home | About | Law | Family Talk | Science | Religion | Chemistry | Biology | Ethics | Halal Businesses</div>
  <div class="links" style="top:39px">How It Works | Trust, Safety &amp; Insurance | Experience Levels | Ratings | Ladies Only | Frequently Asked Questions | Member stories | Contact</div>
  <div class="icons">
    <span style="background:#e1457e"></span><span style="background:#1ea5dc"></span><span style="background:#3b5998"></span><span style="background:#2e7d32"></span><span style="background:#3ea9dd"></span><span style="background:#f29425"></span>
  </div>
</footer>
<div class="copyright">Copyright 2016 Quill Harbour. All Rights Reserved.</div>

</body>
</html>
```